Design a box for EV Charging Cables - Electric Cars

https://files.plomtrex.example/doc/7qRwLm2ZxNa9/view

We are looking to design a box to package our EV charging cables. This box needs to be 40cm x 40cm x 11cm.

It needs to include:
- Our logo
- Images of our products
- Accreditations

My websites are:
https://voltharbor.co.uk/
https://www.plugmerrow.co.uk/
https://www.zandrel-amp.co.uk/

Logo:
https://pixdrop.example/Kq8Tz2L
https://pixdrop.example/Rw4Hn9B
https://pixdrop.example/Jd7Pv3X
https://pixdrop.example/Ny6Qb5G

Rather than having a list of products. I would like to have tick boxes:
1st tick box: Connector Type From: (Type 2, 3 Pin),
2nd tick box: Connector Type To: (Type 1, Type 2),
3rd tick box: Amp/Charge Speed (13amp/16amp/32amp/32amp - 3 Phase)
4th tick box: Length (5m/10m/15m)

Target Market(s)

People who own electric cars

Industry/Entity Type

Automotive

Colors

Designer to choose colors to be used in the design.

Requirements
Must have
• Our colours, logo, list of products we sell
Nice to have
• Rather than having a list of products. I would like to have tick boxes: 1st tick box should be: Connector Type From: (Type 2, 3 Pin), Connector Type To: (Type 1, Type 2), Third: Amp/Charge Speed (13amp/16amp/32amp/32amp - 3 Phase) Third: Length (5m/10m/15m)
Should not have
• Transparent Section

```html
<!DOCTYPE html>
<html lang="en">
<head>
<meta charset="utf-8">
<title>Zandrel Amp – Charging Cable Box Front</title>
<link rel="stylesheet" href="https://fonts.googleapis.com/css2?family=Audiowide&family=Russo+One&family=Saira+Condensed:wght@400;600&display=swap">
<style>
  :root {
    --black: #000000;
    --lime: #a3e05a;
    --green-line: #3fc24d;
    --green-deep: #041d0a;
    --green-mid: #0f5a22;
    --green-bright: #35b44e;
    --white: #ffffff;
    --option-fill: #0a2a10;
    --photo-dark: #101512;
  }
  * { margin: 0; padding: 0; box-sizing: border-box; }
  html, body { width: 1200px; height: 1200px; overflow: hidden; background: var(--black); }
  .box-front {
    position: relative; width: 1200px; height: 1200px; overflow: hidden; background: var(--black);
    font-family: "Saira Condensed", "Arial Narrow", sans-serif; color: var(--white);
  }
  .brand {
    position: absolute; top: 80px; left: 400px; width: 480px; text-align: center;
    font-family: "Audiowide", sans-serif; font-size: 62px; line-height: 1;
    color: var(--lime); letter-spacing: 4px;
  }
  .brand-sub { display: block; margin-top: 26px; font-size: 42px; letter-spacing: 28px; padding-left: 28px; }
  .product-panel {
    position: absolute; left: 0; top: 290px; width: 1200px; height: 910px; overflow: hidden;
    border-top: 4px solid var(--green-line);
    background:
      radial-gradient(ellipse 75% 65% at 80% 88%, var(--green-bright) 0%, var(--green-mid) 45%, transparent 80%),
      linear-gradient(160deg, var(--green-mid) 0%, var(--green-deep) 35%, #072a0f 70%, var(--green-mid) 100%);
  }
  .title {
    position: absolute; left: 84px; top: 36px;
    font-family: "Russo One", sans-serif; font-size: 86px; line-height: 100px;
    letter-spacing: 6px; text-transform: uppercase;
  }
  .product-photo {
    position: absolute; left: 510px; top: 150px; width: 690px; height: 660px;
    border-radius: 46% 0 0 40%;
    background: radial-gradient(ellipse at 45% 50%, var(--photo-dark) 0%, #1b2a1e 55%, rgba(76,220,92,0.35) 85%, transparent 100%);
  }
  .options { position: absolute; left: 66px; top: 430px; width: 260px; }
  .option-group { margin-bottom: 12px; }
  .option-label { font-size: 12px; line-height: 14px; text-transform: uppercase; color: var(--lime); margin-bottom: 8px; }
  .option-row { display: flex; gap: 6px; }
  .option { display: flex; flex-direction: column; align-items: flex-start; gap: 5px; }
  .option-tile {
    width: 52px; height: 58px; border: 1.5px solid var(--lime); background: var(--option-fill);
    display: flex; flex-direction: column; align-items: center; justify-content: center;
    font-weight: 600; color: var(--lime); font-size: 28px; line-height: 1;
  }
  .option-tile small { font-size: 15px; }
  .option-tile .tiny { font-size: 9px; margin-top: 2px; }
  .check { display: flex; align-items: center; gap: 5px; height: 12px; font-size: 10px; color: var(--lime); }
  .check::before { content: ""; width: 11px; height: 11px; border-radius: 50%; background: var(--white); }
</style>
</head>
<body>
<main class="box-front">
  <div class="brand">ZANDREL<span class="brand-sub">AMP</span></div>

  <section class="product-panel">
    <h1 class="title">Charging<br>Cable</h1>

    <div class="product-photo" role="img" aria-label="Product photo: coiled black EV charging cable with green and black Type 1 and Type 2 connector plugs and caps"></div>

    <div class="options">
      <div class="option-group">
        <p class="option-label">Connector type from</p>
        <div class="option-row">
          <div class="option"><div class="option-tile" role="img" aria-label="Type 2 connector icon"></div><span class="check">Type 2</span></div>
          <div class="option"><div class="option-tile" role="img" aria-label="3 pin plug icon"></div><span class="check">3 Pin</span></div>
        </div>
      </div>
      <div class="option-group">
        <p class="option-label">Connector type to</p>
        <div class="option-row">
          <div class="option"><div class="option-tile" role="img" aria-label="Type 1 connector icon"></div><span class="check">Type 1</span></div>
          <div class="option"><div class="option-tile" role="img" aria-label="Type 2 connector icon"></div><span class="check">Type 2</span></div>
        </div>
      </div>
      <div class="option-group">
        <p class="option-label">Length</p>
        <div class="option-row">
          <div class="option"><div class="option-tile">5m</div><span class="check"></span></div>
          <div class="option"><div class="option-tile">10m</div><span class="check"></span></div>
          <div class="option"><div class="option-tile">15m</div><span class="check"></span></div>
        </div>
      </div>
      <div class="option-group">
        <p class="option-label">Amp/charge speed</p>
        <div class="option-row">
          <div class="option"><div class="option-tile">13<small>amp</small></div><span class="check"></span></div>
          <div class="option"><div class="option-tile">16<small>amp</small></div><span class="check"></span></div>
          <div class="option"><div class="option-tile">32<small>amp</small></div><span class="check"></span></div>
          <div class="option"><div class="option-tile">32<span class="tiny">amp/3 Phase</span></div><span class="check"></span></div>
        </div>
      </div>
    </div>
  </section>
</main>
</body>
</html>
```